Business Card Design

Please see my website www.qvloreming.com.au to for further information on my services and styling of my site

Reason: Deadline is extended to permit alterations to current designs or for any new submissions. Cheers

Industry/Entity Type

Business

Contact Information for Business Card

Marcus Thorne
Empowerment Coach

'Live your passion'

marcus@qvtraining.com.au
0437158204
qvtraining.com.au

```html
<!DOCTYPE html>
<html lang="en">
<head>
<meta charset="utf-8">
<title>QVT Business Card</title>
<link rel="stylesheet" href="https://fonts.googleapis.com/css2?family=Oswald:wght@400;600&family=Archivo+Black&display=swap">
<style>
  :root {
    --backdrop: #3b3b3b;
    --card-white: #fbfbfb;
    --brand-green: #8cc63f;
    --panel-green: #4f7d1f;
    --stripe-grey: #b5b5b5;
    --ink-grey: #8a8a8a;
    --ink-dark: #2b2b2b;
    --white: #ffffff;
  }
  * { box-sizing: border-box; margin: 0; padding: 0; }
  html, body { width: 1200px; height: 874px; overflow: hidden; }
  body {
    background: var(--backdrop);
    display: flex;
    align-items: center;
    justify-content: center;
    gap: 60px;
    font-family: "Oswald", sans-serif;
  }
  .card {
    position: relative;
    width: 500px;
    height: 304px;
    border-radius: 3px;
    overflow: hidden;
    box-shadow: 0 10px 30px rgba(0,0,0,.35);
  }

  /* Front */
  .card--front { background: var(--card-white); }
  .front__stripes {
    position: absolute;
    left: 0;
    top: 196px;
    width: 230px;
    display: flex;
    flex-direction: column;
    gap: 5px;
  }
  .stripe { height: 11px; background: var(--brand-green); }
  .stripe--thin { height: 4px; background: var(--stripe-grey); }
  .front__brand {
    position: absolute;
    left: 262px;
    top: 74px;
    width: 200px;
  }
  .brand-mark {
    display: flex;
    align-items: center;
    gap: 10px;
    color: var(--brand-green);
    font-weight: 400;
    font-size: 52px;
    line-height: 1;
    letter-spacing: 2px;
  }
  .brand-mark__square {
    width: 22px; height: 22px;
    background: currentColor;
  }
  .brand-rule {
    height: 2px;
    background: var(--ink-grey);
    margin: 8px 0 6px;
  }
  .brand-name {
    color: var(--brand-green);
    font-size: 15px;
    font-weight: 400;
    letter-spacing: .5px;
  }
  .front__web {
    display: flex;
    align-items: center;
    gap: 5px;
    margin-top: 6px;
    color: var(--ink-dark);
    font-size: 11px;
  }

  /* Back */
  .card--back { background: var(--brand-green); }
  .back__brand {
    position: absolute;
    left: 34px;
    top: 150px;
    width: 190px;
  }
  .back__brand .brand-mark,
  .back__brand .brand-name { color: var(--white); }
  .back__brand .brand-rule { background: var(--white); }
  .contact-panel {
    position: absolute;
    left: 262px;
    right: 14px;
    top: 32px;
    height: 112px;
    background: var(--panel-green);
    border-radius: 10px;
    color: var(--white);
    padding: 12px 16px;
  }
  .contact-panel__name {
    font-family: "Archivo Black", sans-serif;
    font-size: 15px;
    letter-spacing: 2px;
    text-align: center;
  }
  .contact-panel__role,
  .contact-panel__motto {
    font-size: 10px;
    text-align: center;
    line-height: 1.35;
    opacity: .9;
  }
  .contact-panel__details {
    display: grid;
    grid-template-columns: auto 1fr;
    column-gap: 14px;
    margin-top: 8px;
    font-size: 9.5px;
  }
  .contact-line { display: flex; align-items: center; gap: 4px; }
  .contact-line--right { justify-content: flex-end; }
  .contact-line svg { flex: none; }
</style>
</head>
<body>

  <section class="card card--front" aria-label="Card front">
    <div class="front__stripes">
      <div class="stripe"></div>
      <div class="stripe stripe--thin"></div>
      <div class="stripe"></div>
    </div>
    <div class="front__brand">
      <div class="brand-mark"><span>QVT</span><span class="brand-mark__square"></span></div>
      <div class="brand-rule"></div>
      <div class="brand-name">Quest Vitality Training</div>
      <div class="front__web">
        <svg width="10" height="10" viewBox="0 0 10 10" aria-hidden="true">
          <circle cx="5" cy="5" r="4.2" fill="none" stroke="#2b2b2b" stroke-width="1"/>
          <ellipse cx="5" cy="5" rx="1.8" ry="4.2" fill="none" stroke="#2b2b2b" stroke-width=".8"/>
          <line x1=".8" y1="5" x2="9.2" y2="5" stroke="#2b2b2b" stroke-width=".8"/>
        </svg>
        <span>qvtraining.com.au</span>
      </div>
    </div>
  </section>

  <section class="card card--back" aria-label="Card back">
    <div class="contact-panel">
      <div class="contact-panel__name">MARCUS THORNE</div>
      <div class="contact-panel__role">Empowerment Coach</div>
      <div class="contact-panel__motto">'Live your passion'</div>
      <div class="contact-panel__details">
        <div class="contact-line">
          <svg width="8" height="11" viewBox="0 0 8 11" aria-hidden="true">
            <rect x=".5" y=".5" width="7" height="10" rx="1.4" fill="none" stroke="#fff"/>
            <line x1="3" y1="8.6" x2="5" y2="8.6" stroke="#fff"/>
          </svg>
          <span>0437158204</span>
        </div>
        <div class="contact-line contact-line--right">
          <svg width="11" height="8" viewBox="0 0 11 8" aria-hidden="true">
            <rect x=".5" y=".5" width="10" height="7" fill="none" stroke="#fff"/>
            <polyline points=".5,.5 5.5,4.5 10.5,.5" fill="none" stroke="#fff"/>
          </svg>
          <span>marcus@qvtraining.com.au</span>
        </div>
        <div></div>
        <div class="contact-line contact-line--right">
          <svg width="10" height="10" viewBox="0 0 10 10" aria-hidden="true">
            <circle cx="5" cy="5" r="4.2" fill="none" stroke="#fff" stroke-width="1"/>
            <ellipse cx="5" cy="5" rx="1.8" ry="4.2" fill="none" stroke="#fff" stroke-width=".8"/>
            <line x1=".8" y1="5" x2="9.2" y2="5" stroke="#fff" stroke-width=".8"/>
          </svg>
          <span>qvtraining.com.au</span>
        </div>
      </div>
    </div>
    <div class="back__brand">
      <div class="brand-mark"><span>QVT</span><span class="brand-mark__square"></span></div>
      <div class="brand-rule"></div>
      <div class="brand-name">Quest Vitality Training</div>
    </div>
  </section>

</body>
</html>
```